New Homepage for young Boston startup

We want a new website design for our company. We need you to design the homepage for it. If your design is chosen we may ask you also to design the website template page that is used for all secondary pages, Blog template page & Email template for email newsletter.

end deliverable in this stage is homepage only in both PSD/AI and JPG. Please see the attached document for detailed requirements of the job to be done.

the attachment contains a suggested wireframe (if you feel things are missing or things are redundant feel free to add them or leave them out of the design. Please also have a look at our existing homepage (www.brixaprep.vq), although we love to have a fresher design.

Examples of websites we very much like:
http://www.mulo.vq/
www.fitrund.com
https://vobe.com

Made a small mistake in the link to a website that I really like. It should have been: http://www.mulo.vq/

instead of mulovq.com which is horrible :)

Reason: I've extended the deadline to give some of you more time to finish your work.

Target Market(s)

We build a mobile solution for studying the KVEX test. Our target audience are College educated people 20-35 years old, interested in studying for the KVEX as they need to apply for a school that requires the KVEX (most international MBA's do).

Industry/Entity Type

It Company

Requirements
Must have
• complete homepage design with the elements from the wireframe document.

```html
<!DOCTYPE html>
<html lang="en">
<head>
<meta charset="utf-8">
<title>Brixa Exam Prep Platform</title>
<link href="https://fonts.googleapis.com/css2?family=Roboto:ital,wght@0,300;0,400;0,500;0,700;1,400&family=Dancing+Script&display=swap" rel="stylesheet">
<style>
:root{
  --topbar:#3b3b3b;
  --header:#333333;
  --accent:#1fa3e6;
  --ink:#333333;
  --light:#f5f5f5;
  --light2:#f7f7f7;
  --white:#ffffff;
  --green:#a4c83a;
  --orange:#f28322;
  --red:#e8502a;
  --pink:#d8245f;
  --rule-orange:#e37b2c;
  --icon-blue:#4fb3ea;
}
*{box-sizing:border-box;margin:0;padding:0}
html,body{width:1200px;height:2624px;overflow:hidden}
body{font-family:"Roboto",Arial,sans-serif;color:var(--ink);background:var(--white);position:relative}
.abs{position:absolute}

/* top bar */
.topbar{position:absolute;left:0;top:0;width:1200px;height:31px;background:var(--topbar);color:#cfcfcf;font-size:11px}
.topbar .item{position:absolute;top:9px;display:flex;align-items:center;gap:6px}

/* header */
.header{position:absolute;left:0;top:31px;width:1200px;height:97px;background:var(--header)}
.brand{position:absolute;left:189px;top:22px;display:flex;align-items:center;gap:10px}
.brand-mark{width:40px;height:40px;background:var(--red)}
.brand-name{color:var(--white);font-size:30px;font-weight:500;line-height:1}
.brand-sub{position:absolute;left:239px;top:62px;color:#cccccc;font-size:11px;font-weight:500}
.nav{position:absolute;top:40px;left:600px;display:flex;gap:24px;font-size:13px;font-weight:400;color:var(--white)}
.nav .active{color:var(--accent)}

/* hero */
.hero{position:absolute;left:0;top:128px;width:1200px;height:477px;background:linear-gradient(90deg,#3d4a57 0%,#6d7f90 40%,#aab6c1 70%,#7d8d9b 100%)}
.hero-photo{position:absolute;inset:0}
.hero-title{position:absolute;left:189px;top:146px;color:var(--white);font-size:24px;font-weight:400}
.hero-title b{font-weight:700}
.hero-text{position:absolute;left:189px;top:183px;width:360px;color:#eeeeee;font-size:13px;line-height:19px}
.store-btn{position:absolute;top:253px;width:161px;height:57px;display:flex;align-items:center;gap:12px;padding-left:14px;color:var(--white);font-size:11px;line-height:14px}
.store-btn.dark{left:189px;background:#1b1b1b}
.store-btn.blue{left:359px;background:var(--accent)}
.store-btn .dot{width:22px;height:22px;border-radius:50%;background:var(--white)}
.store-note{position:absolute;top:317px;color:var(--white);font-family:"Dancing Script",cursive;font-size:14px}
.hero-arrow{position:absolute;top:218px;width:45px;height:45px;border:2px solid var(--white);border-radius:50%}

/* email band */
.signup{position:absolute;left:0;top:605px;width:1200px;height:202px;background:var(--light)}
.signup-lead{position:absolute;top:54px;width:1200px;text-align:center;font-size:23px;font-weight:300;color:#777777}
.signup-input{position:absolute;left:432px;top:104px;width:208px;height:38px;background:var(--white);color:#bbbbbb;font-size:12px;padding:12px 16px}
.signup-btn{position:absolute;left:640px;top:104px;width:128px;height:38px;background:var(--accent);color:var(--white);font-size:16px;text-align:center;line-height:38px}

/* section headings */
.section-title{position:absolute;font-size:32px;font-weight:300;color:var(--ink)}
.rule{position:absolute;height:2px;width:50px;background:var(--accent)}

/* services */
.services{position:absolute;left:0;top:807px;width:1200px;height:511px;background:var(--white)}
.service{position:absolute;top:162px;width:200px;text-align:center}
.service-icon{width:78px;height:78px;margin:0 auto;border-radius:50%;border:2px solid;display:flex;align-items:center;justify-content:center}
.service h3{margin-top:20px;font-size:17px;font-weight:300;line-height:22px;color:#555555}
.service p{width:176px;margin:22px auto 0;font-size:11px;line-height:19px;color:#555555}
.service a{display:block;margin-top:10px;font-size:11px;color:var(--accent);text-decoration:none}

/* why us */
.why{position:absolute;left:0;top:1318px;width:1200px;height:555px;background:var(--light2)}
.reason{position:absolute;left:189px;width:480px;display:flex;gap:38px;align-items:flex-start}
.reason svg{flex:none}
.reason p{font-size:11px;line-height:19px;color:#444444;padding-top:6px}
.quote-line{position:absolute;left:728px;width:284px;height:1px;background:#e3e3e3}
.quote-mark{position:absolute;left:851px;top:172px;width:38px;height:38px;border-radius:50%;background:var(--white);border:1px solid #dddddd;color:var(--accent);font-size:24px;font-weight:700;text-align:center;line-height:44px}
.quote-text{position:absolute;left:758px;top:222px;width:224px;text-align:center;font-style:italic;font-size:11px;line-height:17px;color:#777777}
.avatar{position:absolute;left:844px;top:340px;width:52px;height:52px;border-radius:50%;background:var(--accent);border:3px solid var(--white)}
.quote-name{position:absolute;left:728px;top:404px;width:284px;text-align:center;font-size:11px;font-weight:700;color:#2a4a6a}

/* contact */
.contact{position:absolute;left:0;top:1873px;width:1200px;height:554px;background:linear-gradient(120deg,#2a6a98 0%,#1f5e8a 45%,#3f7ea8 75%,#1d5580 100%)}
.contact .section-title{color:var(--white)}
.contact-rule{position:absolute;left:575px;top:138px;width:50px;height:2px;background:var(--rule-orange)}
.contact-sub{position:absolute;left:189px;top:200px;color:var(--white);font-size:18px;font-weight:300}
.contact-text{position:absolute;left:189px;top:233px;width:350px;color:var(--white);font-size:11px;line-height:19px}
.contact-row{position:absolute;left:189px;display:flex;align-items:center;gap:24px;color:var(--white);font-size:11px}
.field{position:absolute;background:var(--white);color:#c7c7c7;font-size:11px;padding:10px 12px}
.send-btn{position:absolute;left:873px;top:431px;width:137px;height:38px;background:var(--accent);color:var(--white);font-size:13px;text-align:center;line-height:38px}

/* footer */
.footer{position:absolute;left:0;top:2427px;width:1200px;height:197px;background:var(--white)}
.social{position:absolute;top:44px;width:34px;height:34px;border-radius:50%}
.copyright{position:absolute;top:101px;width:1200px;text-align:center;font-size:11px;color:#888888}
.to-top{position:absolute;left:1021px;top:40px;width:44px;height:44px;border-radius:50%;background:#f0f0f0}
.color-strip{position:absolute;left:0;bottom:0;width:1200px;height:5px;display:flex}
.color-strip span{flex:1}
</style>
</head>
<body>

<div class="topbar">
  <div class="item" style="left:721px">
    <svg width="13" height="10" viewBox="0 0 13 10"><rect x="0" y="0" width="13" height="10" fill="#cfcfcf"/><path d="M0 0 L6.5 5 L13 0" stroke="#3b3b3b" fill="none"/></svg>
    info@brixaprep.vq
  </div>
  <div class="item" style="left:875px">
    <svg width="11" height="11" viewBox="0 0 11 11"><circle cx="5.5" cy="5.5" r="5.5" fill="#cfcfcf"/></svg>
    www.brixaprep.vq
  </div>
</div>

<header class="header">
  <div class="brand"><div class="brand-mark"></div><div class="brand-name">Brixa</div></div>
  <div class="brand-sub">Exam Prep Platform</div>
  <nav class="nav">
    <span class="active">Home</span><span>Blog</span><span>About Us</span><span>Products</span><span>Careers</span><span>Contact Us</span>
  </nav>
</header>

<section class="hero">
  <div class="hero-photo" role="img" aria-label="Photo of a hand holding a white smartphone in front of a blurred blue sea background"></div>
  <h1 class="hero-title"><b>Brixa</b> Exam Prep Platform</h1>
  <p class="hero-text">We have createdBrixa KVEX as the most comprehensiveK-VEX preparationsystem. It's a full course in a mobile app.</p>
  <div class="store-btn dark"><span class="dot"></span><span>Download on the<br>APP MARKET</span></div>
  <div class="store-btn blue"><span class="dot"></span><span>Download on the<br>APP MARKET</span></div>
  <div class="store-note" style="left:191px">English Phone version</div>
  <div class="store-note" style="left:359px">Chinese Phone Version</div>
  <div class="hero-arrow" style="left:39px">
    <svg width="41" height="41" viewBox="0 0 41 41"><path d="M23 14 L17 20.5 L23 27" stroke="#fff" stroke-width="2" fill="none"/></svg>
  </div>
  <div class="hero-arrow" style="left:1116px">
    <svg width="41" height="41" viewBox="0 0 41 41"><path d="M18 14 L24 20.5 L18 27" stroke="#fff" stroke-width="2" fill="none"/></svg>
  </div>
</section>

<section class="signup">
  <p class="signup-lead">Leave your e-mail address and we'll send you a download link</p>
  <div class="signup-input">Email Address</div>
  <div class="signup-btn">Submit</div>
</section>

<section class="services">
  <h2 class="section-title" style="top:66px;left:0;width:1200px;text-align:center">Our Service</h2>
  <div class="rule" style="left:575px;top:112px"></div>

  <div class="service" style="left:192px">
    <div class="service-icon" style="border-color:var(--green)">
      <svg width="30" height="30" viewBox="0 0 30 30" fill="none" stroke="#a4c83a" stroke-width="2"><rect x="4" y="5" width="5" height="12"/><path d="M9 6 H21 L24 16 H17 L18 25 L14 25 L9 16"/></svg>
    </div>
    <h3>Our<br>Ineffective</h3>
    <p>Lorem Ipsum is simply dummy text of the printing and typesetting industry. Lorem Ipsum has</p>
    <a href="#">Read More</a>
  </div>

  <div class="service" style="left:397px">
    <div class="service-icon" style="border-color:var(--orange)">
      <svg width="30" height="30" viewBox="0 0 30 30" fill="none" stroke="#f28322" stroke-width="2"><rect x="3" y="6" width="24" height="15"/><path d="M11 25 H19 M15 21 V25"/></svg>
    </div>
    <h3>Our<br>Expensive</h3>
    <p>Lorem Ipsum is simply dummy text of the printing and typesetting industry. Lorem Ipsum has</p>
    <a href="#">Read More</a>
  </div>

  <div class="service" style="left:602px">
    <div class="service-icon" style="border-color:var(--red);background:var(--red)">
      <svg width="30" height="30" viewBox="0 0 30 30" fill="none" stroke="#fff" stroke-width="2"><circle cx="15" cy="12" r="7"/><path d="M12 19 V23 H18 V19 M13 26 H17"/></svg>
    </div>
    <h3>No detailed &amp;<br>actionable analytics</h3>
    <p>Lorem Ipsum is simply dummy text of the printing and typesetting industry. Lorem Ipsum has</p>
    <a href="#">Read More</a>
  </div>

  <div class="service" style="left:806px">
    <div class="service-icon" style="border-color:var(--pink)">
      <svg width="30" height="30" viewBox="0 0 30 30" fill="none" stroke="#d8245f" stroke-width="2"><rect x="9" y="4" width="12" height="22" rx="2"/><path d="M13 22 H17"/></svg>
    </div>
    <h3>No serious<br>mobile solution</h3>
    <p>Lorem Ipsum is simply dummy text of the printing and typesetting industry. Lorem Ipsum has</p>
    <a href="#">Read More</a>
  </div>
</section>

<section class="why">
  <h2 class="section-title" style="left:189px;top:80px">Why should they choose us ?</h2>
  <div class="rule" style="left:368px;top:130px"></div>

  <div class="reason" style="top:176px">
    <svg width="46" height="58" viewBox="0 0 46 58"><rect x="2" y="2" width="42" height="54" rx="4" fill="none" stroke="#a4c83a" stroke-width="3"/><circle cx="23" cy="50" r="2" fill="#a4c83a"/></svg>
    <p>The Label StudyingMethodTMhelpsyouidentifythe conceptsthatwillbetestedin the KVEX. It acts likeanX-rayforthe KVEX questions. Bylearningtoidentifythe conceptsthatare beingtested, youwillbeabletofindthe right answerfaster.</p>
  </div>
  <div class="reason" style="top:274px">
    <svg width="46" height="58" viewBox="0 0 46 58"><rect x="2" y="2" width="42" height="54" rx="4" fill="none" stroke="#f28322" stroke-width="3"/><circle cx="23" cy="50" r="2" fill="#f28322"/></svg>
    <p style="padding-top:22px">Studythe conceptsusinghundredsof flashcards</p>
  </div>
  <div class="reason" style="top:370px">
    <svg width="46" height="58" viewBox="0 0 46 58"><rect x="2" y="2" width="42" height="54" rx="4" fill="none" stroke="#e8502a" stroke-width="3"/><circle cx="23" cy="50" r="2" fill="#e8502a"/></svg>
    <p>Studyon the move! The Brixa KVEX mobile appworksoffline, soletsyoustudy-forthe KVEX wheneverandwhereveryouwant. Whetheryouare on a planeor in a train or have sometime tospareduringyourbreak.</p>
  </div>

  <h2 class="section-title" style="left:728px;top:80px">Client Testimonials</h2>
  <div class="rule" style="left:838px;top:130px"></div>
  <div class="quote-line" style="top:190px"></div>
  <div class="quote-mark">&ldquo;</div>
  <p class="quote-text">Lorem Ipsum is simply dummy text of the printing and typesetting industry. Lorem Ipsum has been the industry's standard dummy text ever since the 1500s, when an unknown printer took a galley of type and scrambled it to make a type</p>
  <div class="quote-line" style="top:366px"></div>
  <div class="avatar" role="img" aria-label="Client portrait placeholder"></div>
  <div class="quote-name">NORA VELL</div>
</section>

<section class="contact">
  <div class="abs" style="inset:0" role="img" aria-label="Blue-tinted photo of a person working at a laptop"></div>
  <h2 class="section-title" style="left:0;top:80px;width:1200px;text-align:center">Contact Us</h2>
  <div class="contact-rule"></div>
  <h3 class="contact-sub">Get in touch with us</h3>
  <p class="contact-text">Lorem Ipsum is simply dummy text of the printing and typesetting industry. Lorem Ipsum has been the industry's standard dummy text</p>
  <div class="contact-row" style="top:299px">
    <svg width="20" height="16" viewBox="0 0 20 16"><path d="M10 0 L20 8 H17 V16 H12 V11 H8 V16 H3 V8 H0 Z" fill="#4fb3ea"/></svg>
    www.brixaprep.vq
  </div>
  <div class="contact-row" style="top:337px">
    <svg width="20" height="16" viewBox="0 0 20 16"><path d="M4 1 L8 4 L6 7 Q8 11 12 12 L14 9 L18 12 L16 15 Q6 15 2 4 Z" fill="#4fb3ea"/></svg>
    +81- 5550- 123 4567
  </div>
  <div class="contact-row" style="top:372px">
    <svg width="20" height="16" viewBox="0 0 20 16"><rect x="1" y="2" width="18" height="12" fill="#4fb3ea"/><path d="M1 2 L10 9 L19 2" stroke="#1f5e8a" fill="none"/></svg>
    info@brixaprep.vq
  </div>
  <div class="field" style="left:600px;top:205px;width:193px;height:34px">Name *</div>
  <div class="field" style="left:817px;top:205px;width:193px;height:34px">Email *</div>
  <div class="field" style="left:600px;top:264px;width:410px;height:145px">Message *</div>
  <div class="send-btn">Send</div>
</section>

<footer class="footer">
  <div class="social" style="left:536px;background:#3b5998"></div>
  <div class="social" style="left:583px;background:#2fa9e0"></div>
  <div class="social" style="left:627px;background:#dd4b39"></div>
  <div class="to-top">
    <svg width="44" height="44" viewBox="0 0 44 44"><path d="M15 25 L22 18 L29 25" stroke="#c8c8c8" stroke-width="2" fill="none"/></svg>
  </div>
  <p class="copyright">Copyright &copy; 2013 All right Reserved www.brixaprep.vq</p>
  <div class="color-strip">
    <span style="background:var(--green)"></span><span style="background:var(--orange)"></span><span style="background:var(--red)"></span><span style="background:var(--pink)"></span>
  </div>
</footer>

</body>
</html>
```